Global Video

I need a simple design for a simple idea. A one page website for now. No backend. Just looking for a design that translates the power of the idea.
The product I offer is a video made in any geo of the world as requested by the user. The user comes to the site and they see a large map covering most of the page (Google Maps API). The user submits a video request to be filmed in a specific location around the world. Ideally they will do this through the map.

Below the map is a submission form with the following fields which the user completes:

Name:
Email:
Phone:
ZIP of Request:
Request Idea:
$$:

Submit Button - goes to a Google spreadsheet.

These submissions will be turned into the specific video the customer is looking for.

Above the map will be a link that says 'Do you shoot video?' - this will click to another spreadsheet, which aggregates a community of videographers around the globe

We want something very simple and direct. The map is the focal point. The site should somehow imply that something previously not possible now is. Dream big.

Please leave space for a name/logo and feel free to pick the font/colors you feel works best

Reason: I am extending this project and changing it to non-refundable in order to get more quality submissions. Let's see what you got!

Community

• An interactive map.
A submission form.

```html
<!DOCTYPE html>
<html lang="en">
<head>
<meta charset="utf-8">
<title>Global Video</title>
<link rel="stylesheet" href="https://fonts.googleapis.com/css2?family=Oswald:wght@500;600&family=Source+Sans+3:wght@300;400;600&family=Yellowtail&display=swap">
<style>
:root{
  --red:#d9584a;
  --blue:#2a6496;
  --ink:#111111;
  --muted:#bfb8b2;
  --field-border:#c9beb1;
  --field-bg:#f7f6f4;
  --field-text:#b8ada2;
  --divider:#bdb2a6;
  --white:#ffffff;
}
*{margin:0;padding:0;box-sizing:border-box}
html,body{width:1200px;height:933px;overflow:hidden;background:var(--white)}
body{position:relative;font-family:"Source Sans 3",sans-serif;color:var(--ink)}
.abs{position:absolute}

.hero-photo{left:0;top:0;width:1200px;height:473px;
  background:linear-gradient(100deg,#6f5a48 0%,#8b7560 30%,#a08a74 55%,#9c8d7b 75%,#7d6f55 100%)}

.site-header{left:117px;top:0;width:959px;height:88px;background:var(--white)}
.brand{left:79px;top:26px;font-size:34px;font-weight:400;letter-spacing:.5px}
.brand-divider{left:245px;top:25px;width:4px;height:39px;background:var(--ink)}
.main-nav{left:291px;top:34px;display:flex;gap:14px;font-size:16px;font-weight:300;color:var(--muted)}
.main-nav .current{color:var(--ink);font-weight:400;margin-right:4px}
.login{left:712px;top:34px;font-size:16px;font-weight:300;color:var(--red)}
.social{left:781px;top:38px;display:flex;gap:21px}
.social span{width:14px;height:14px;border-radius:50%;background:#c6c1bc}

.shooter-link{left:824px;top:88px;width:251px;height:34px;background:var(--red);color:var(--white);
  font-size:16px;letter-spacing:.6px;display:flex;align-items:center;padding-left:39px}
.shooter-link svg{position:absolute;right:22px;top:10px}

.tagline{left:99px;top:309px;width:488px;height:164px;background:var(--red)}
.tag-you{left:50px;top:28px;font-family:"Oswald",sans-serif;font-weight:600;font-size:104px;line-height:1;color:var(--white);letter-spacing:-2px}
.tag-bar{left:215px;top:67px;width:230px;height:14px;background:var(--blue);transform:skewY(-2deg)}
.tag-line{font-family:"Oswald",sans-serif;font-weight:500;color:var(--white);font-size:30px;line-height:1;transform:scaleX(.88);transform-origin:left}
.tag-line.one{left:223px;top:38px}
.tag-line.two{left:233px;top:81px}
.tag-script{left:251px;top:113px;font-family:"Yellowtail",cursive;font-size:31px;color:var(--white)}

.panel-icon{width:48px;height:48px;border-radius:50%}
.city-icon{left:154px;top:512px;background:var(--red)}
.request-icon{left:448px;top:512px;background:var(--ink)}
.panel-title{font-size:21px;font-weight:400}
.city-title{left:220px;top:522px}
.request-title{left:514px;top:524px;font-size:19px}

.city-dropdown{left:156px;top:585px;width:191px;height:38px;border:3px solid var(--field-border);background:var(--field-bg);
  font-size:12px;color:var(--field-text);padding:0 11px;display:flex;align-items:center;justify-content:space-between}
.videographer-count{left:168px;top:649px;font-size:12px;font-weight:600;letter-spacing:-.2px}
.panel-divider{left:393px;top:513px;width:3px;height:205px;background:var(--divider)}

.field{width:195px;height:32px;border:3px solid var(--field-border);background:var(--field-bg);
  font-size:12px;color:var(--field-text);display:flex;align-items:center;justify-content:center}
.submit{left:1011px;top:668px;font-size:12px;color:#9a9289;display:flex;align-items:center;gap:19px}

.map-area{left:0;top:746px;width:1200px;height:187px;
  background:linear-gradient(160deg,#d8d5cf 0%,#ebe8e2 35%,#f1ebd2 55%,#e6dfbf 75%,#d9c28a 100%)}
</style>
</head>
<body>
<div class="abs hero-photo" role="img" aria-label="Photo of a smiling videographer carrying a film camera rig outdoors"></div>

<header class="abs site-header">
  <div class="abs brand">LOGO</div>
  <div class="abs brand-divider"></div>
  <nav class="abs main-nav"><span class="current">HOME</span><span>OTHER</span><span>OTHER</span><span>OTHER</span><span>OTHER</span></nav>
  <div class="abs login">LOGIN</div>
  <div class="abs social"><span></span><span></span><span></span><span></span><span></span></div>
</header>

<a class="abs shooter-link">Do You Shoot Video?
  <svg width="12" height="16" viewBox="0 0 12 16"><path d="M2 1l7 7-7 7" fill="none" stroke="#fff" stroke-width="3"/></svg>
</a>

<div class="abs tagline">
  <div class="abs tag-you">YOU</div>
  <div class="abs tag-bar"></div>
  <div class="abs tag-line one">CAN HAVE FOOTAGE</div>
  <div class="abs tag-line two">FROM ANYWHERE</div>
  <div class="abs tag-script">in the world</div>
</div>

<div class="abs panel-icon city-icon">
  <svg width="48" height="48" viewBox="0 0 48 48"><path d="M24 13a8 8 0 0 0-8 8c0 6 8 14 8 14s8-8 8-14a8 8 0 0 0-8-8z" fill="#fff"/></svg>
</div>
<div class="abs panel-title city-title">City select</div>
<div class="abs city-dropdown">BUCHAREST
  <svg width="16" height="10" viewBox="0 0 16 10"><path d="M2 2l6 6 6-6" fill="none" stroke="#b8ada2" stroke-width="3"/></svg>
</div>
<div class="abs videographer-count">4,089 VIDEOGRAPHERS</div>
<div class="abs panel-divider"></div>

<div class="abs panel-icon request-icon">
  <svg width="48" height="48" viewBox="0 0 48 48"><path d="M21 26l3 9 8-22" fill="none" stroke="#fff" stroke-width="4" stroke-linecap="round" stroke-linejoin="round"/></svg>
</div>
<div class="abs panel-title request-title">Submit a video request</div>

<div class="abs field" style="left:513px;top:574px">NAME</div>
<div class="abs field" style="left:513px;top:616px">E-MAIL</div>
<div class="abs field" style="left:513px;top:653px">PHONE</div>
<div class="abs field" style="left:722px;top:574px">ZIP CODE of REQUEST</div>
<div class="abs field" style="left:722px;top:616px">REQUEST IDEA</div>
<div class="abs field" style="left:722px;top:653px">PAY</div>
<div class="abs submit">SUBMIT
  <svg width="10" height="16" viewBox="0 0 10 16"><path d="M2 1l6 7-6 7" fill="none" stroke="#9a9289" stroke-width="3"/></svg>
</div>

<div class="abs map-area" role="img" aria-label="Interactive street map for choosing a filming location"></div>
</body>
</html>
```